Information One Page for Email

I am looking for a informative attachment I can send with an introductive email for Ridgeview Cable Works. Something I can also Mail.

Ridgeview Cable Works is the leader in Rebar Post Tension Cable Placement and Post Tension Cable repair. Outside of cable placement and repair we do concrete repair, Parking Garage restoration and

Content

Post Tension Repair and Concrete Restoration
Post-tensioning is a revolutionary method in concrete construction that enhances the strength and durability of structures. However, like all construction ele-ments, post-tension cables can experience wear and damage over time. Ensuring timely and effective repair is crucial for maintaining the safety and integrity of your building.
Why Post-Tension Cable Repair is Essential
1. **Structural Integrity**: Damaged or deteriorated cables can compromise the structural integrity of your building, leading to safety hazards and potential structural failures.
2. **Extended Lifespan**: Regular maintenance and repair of post-tension cables extend the lifespan of your structure, ensuring it remains safe and function-al for years to come.
3. **Cost-Effective**: Addressing cable issues early on prevents more severe damage and costly repairs down the line.
Common Signs of Post-Tension Cable Issues
- Cracks in concrete surfaces
- Unusual noises or popping sounds
- Visible cable ends or broken strands
- Water leakage through cracks
Our Repair Process
1. **Inspection and Assessment**: Our team conducts a thorough inspection to identify the extent of the damage and determine the appropriate repair meth-ods.
2. **Cable Repair or Replacement**: Depending on the severity, we either re-pair the existing cables or replace them with new ones to restore full functional-ity.
3. **Sealing and Protection**: After repairing, we seal the affected areas to protect against moisture and future damage.
4. **Quality Assurance**: We perform rigorous quality checks to ensure the repairs meet industry standards and the structure is safe for use.
Why Choose Us
- **Expertise and Experience**: With years of experience in post-tension cable repair, our team is skilled in handling even the most complex repairs efficiently and effectively.
- **Advanced Technology**: We use the latest technology and materials to ensure durable and long-lasting repairs.
- **Customer Satisfaction**: Our commitment to quality and customer satisfaction sets us apart. We work closely with our clients to ensure their needs are met and expectations exceeded.
Contact Us
If you suspect issues with your post-tension cables or need a routine inspection, don't hesitate to contact us. Our experts are ready to provide the best solutions to keep your structures safe and secure.
Ensure the safety and longevity of your building with our professional post-tension cable repair services. Trust us to deliver quality and reliability every time.

```html
<!DOCTYPE html>
<html lang="en">
<head>
<meta charset="UTF-8">
<title>Ridgeview Cable Works – Post Tension Repair and Concrete Restoration</title>
<link href="https://fonts.googleapis.com/css2?family=Poppins:wght@300;400;500;600;700&display=swap" rel="stylesheet">
<style>
  :root{
    --green:#005c31;
    --grey-panel:#808080;
    --grey-text:#6d6e71;
    --light-grey:#d2d3d5;
    --ink:#1d1d1b;
    --page:#ffffff;
    --backdrop:#ececec;
  }
  *{box-sizing:border-box;margin:0;padding:0}
  html,body{width:760px;height:1200px;overflow:hidden;background:var(--backdrop)}
  body{font-family:'Poppins',sans-serif;color:var(--ink)}
  .sheet{position:absolute;left:25px;top:0;width:710px;height:1200px;background:var(--page);overflow:hidden}
  .abs{position:absolute}

  .brand{left:46px;top:52px;display:flex;align-items:center;gap:10px;color:var(--green);font-weight:600;font-size:25px;line-height:29px}
  .brand-square{width:14px;height:14px;background:var(--green);flex:none}

  .photo-parking{left:355px;top:38px;width:355px;height:285px;
    background:linear-gradient(160deg,#c9cbcd 0%,#a9abac 45%,#8d8e8c 100%);
    clip-path:polygon(0 0,355px 0,355px 285px,125px 285px,125px 144px,0 144px)}
  .hero{left:0;top:194px;width:469px;height:171px;background:var(--green);
    clip-path:polygon(0 0,469px 0,469px 103px,406px 103px,406px 171px,0 171px)}
  .hero-title{left:46px;top:208px;font-size:37px;line-height:33px;letter-spacing:-.5px}
  .hero-title .light{display:block;color:var(--light-grey);font-weight:300}
  .hero-title .bold{display:block;color:#fff;font-weight:700}
  .photo-frame{left:406px;top:297px;width:258px;height:188px;background:var(--page)}
  .photo-facade{left:417px;top:308px;width:236px;height:166px;
    background:linear-gradient(180deg,#c4c6c4 0%,#a3a49f 55%,#8a7f66 100%)}

  .intro{left:47px;top:377px;width:362px;font-size:10.5px;line-height:14.2px;letter-spacing:-.1px}

  .section-head{font-weight:600;font-size:19.5px;line-height:20px;border-left:2px solid var(--grey-text);padding-left:10px}
  .section-head .g{color:var(--green)}
  .section-head .s{color:var(--grey-text)}
  .essential-head{left:47px;top:470px}

  .check{position:absolute;left:0;top:1px;width:11px;height:11px}
  .points{font-size:10.5px;line-height:14.2px;letter-spacing:-.1px}
  .points li{list-style:none;position:relative;padding-left:17px}
  .points b{color:var(--green);font-weight:600;display:block}
  .essential{left:46px;top:527px;width:352px}
  .essential li{margin-bottom:10px}

  .signs{left:418px;top:484px;width:236px;height:219px;background:var(--grey-panel);color:#fff}
  .signs h3{font-weight:500;font-size:13.6px;line-height:14.5px;padding:16px 0 0 11px;margin-bottom:8px}
  .signs ul{list-style:none}
  .signs li{display:flex;align-items:center;height:var(--h);border-top:1px solid #9a9a9a;font-size:11px;font-weight:300;line-height:14.2px}
  .signs li:first-child{border-top:none}
  .signs li svg{width:22px;height:22px;margin:0 16px 0 11px;flex:none}

  .process{left:45px;top:715px;width:369px;height:316px;background:var(--green);color:#fff}
  .process h3{position:absolute;left:18px;top:16px;font-weight:600;font-size:19.5px}
  .step{position:absolute;left:18px;width:348px;padding-left:42px;font-size:10.5px;line-height:14.2px;font-weight:300;letter-spacing:-.1px}
  .step b{font-weight:500;display:block}
  .step svg{position:absolute;left:0;top:2px;width:34px;height:34px}

  .choose-head{left:429px;top:730px}
  .choose{left:430px;top:788px;width:246px}
  .choose li{padding-bottom:10px;margin-bottom:11px;border-bottom:1px solid #e3e3e3}
  .choose li:last-child{border-bottom:none}

  .closing{left:45px;width:615px;font-size:8.8px;line-height:12px}

  .contact-head{left:45px;top:1130px;font-weight:600;font-size:20px;line-height:20px}
  .contact-head .g{color:var(--green);display:block}
  .contact-head .s{color:var(--grey-text);display:block}
  .contact-line{left:178px;display:flex;align-items:center;gap:7px;font-size:13px;font-weight:500;color:var(--ink)}
  .contact-line svg{width:11px;height:11px}
  .web{left:431px;top:1134px;width:225px;height:26px;background:var(--green);color:#fff;font-weight:600;font-size:11.6px;display:flex;align-items:center;justify-content:center}
</style>
</head>
<body>
<main class="sheet">
  <div class="abs brand"><span class="brand-square"></span><span>Ridgeview<br>Cable Works</span></div>

  <div class="abs photo-parking" role="img" aria-label="Photo of a concrete parking deck beside a high-rise condominium"></div>
  <div class="abs hero"></div>
  <h1 class="abs hero-title">
    <span class="light">POST TENSION</span>
    <span class="light">REPAIR AND</span>
    <span class="bold">CONCRETE</span>
    <span class="bold">RESTORATION</span>
  </h1>
  <div class="abs photo-frame"></div>
  <div class="abs photo-facade" role="img" aria-label="Photo of a curved building facade under concrete restoration with a suspended work platform"></div>

  <p class="abs intro">Post-tensioning is a revolutionary method in concrete construction that enhances the strength and durability of structures. However, like all construction ele-ments, post-tension cables can experience wear and damage over time. Ensuring timely and effective repair is crucial for maintaining the safety and integrity of your building.</p>

  <h2 class="abs section-head essential-head"><span class="g">WHY POST-TENSION CABLE</span><br><span class="s">REPAIR IS ESSENTIAL</span></h2>

  <ul class="abs points essential">
    <li><svg class="check" viewBox="0 0 12 12"><circle cx="6" cy="6" r="6" fill="#005c31"/><path d="M3.2 6.2l2 2 3.6-4" stroke="#fff" stroke-width="1.6" fill="none"/></svg><b>Structural Integrity:</b>Damaged or deteriorated cables can compromise the structural integrity of your building, leading to safety hazards and potential structural failures.</li>
    <li><svg class="check" viewBox="0 0 12 12"><circle cx="6" cy="6" r="6" fill="#005c31"/><path d="M3.2 6.2l2 2 3.6-4" stroke="#fff" stroke-width="1.6" fill="none"/></svg><b>Extended Lifespan:</b>Regular maintenance and repair of post-tension cables extend the lifespan of your structure, ensuring it remains safe and function-al for years to come.</li>
    <li><svg class="check" viewBox="0 0 12 12"><circle cx="6" cy="6" r="6" fill="#005c31"/><path d="M3.2 6.2l2 2 3.6-4" stroke="#fff" stroke-width="1.6" fill="none"/></svg><b>Cost-Effective:</b>Addressing cable issues early on prevents more severe damage and costly repairs down the line.</li>
  </ul>

  <section class="abs signs">
    <h3>COMMON SIGNS OF<br>POST-TENSION CABLE ISSUES</h3>
    <ul>
      <li style="--h:36px"><svg viewBox="0 0 24 24" fill="none" stroke="#fff" stroke-width="1.6"><rect x="3" y="3" width="18" height="18"/><path d="M12 3l-2 6 3 3-2 5 1 4"/></svg>Cracks in concrete surfaces</li>
      <li style="--h:40px"><svg viewBox="0 0 24 24" fill="#fff"><path d="M3 19l9-11 4 4-11 9z"/><path d="M15 3v3M19 5l-2 2M21 9h-3" stroke="#fff" stroke-width="1.6"/></svg>Unusual noises or popping<br>sounds</li>
      <li style="--h:46px"><svg viewBox="0 0 24 24" fill="#fff"><rect x="3" y="10" width="4" height="11"/><rect x="10" y="8" width="4" height="13"/><path d="M17 21V11M19 21v-8M17 8l-1-4M19 8l2-4" stroke="#fff" stroke-width="1.6"/></svg>Visible cable ends or<br>broken strands</li>
      <li style="--h:50px"><svg viewBox="0 0 24 24" fill="#fff"><rect x="9" y="2" width="6" height="4"/><rect x="4" y="7" width="16" height="5"/><path d="M8 15l-1 3M12 15v4M16 15l1 3" stroke="#fff" stroke-width="1.6"/></svg>Water leakage through<br>cracks</li>
    </ul>
  </section>

  <section class="abs process">
    <h3>OUR REPAIR PROCESS</h3>
    <div class="step" style="top:52px"><svg viewBox="0 0 34 34" fill="none" stroke="#fff" stroke-width="1.8"><path d="M3 14L17 3l14 11"/><path d="M7 12v18h20V12"/><circle cx="14" cy="19" r="5"/><path d="M18 23l5 5"/></svg><b>Inspection and Assessment:</b>Our team conducts a thorough inspection to identify the extent of the damage and determine the appropriate repair meth-ods.</div>
    <div class="step" style="top:123px"><svg viewBox="0 0 34 34" fill="none" stroke="#fff" stroke-width="1.8"><rect x="4" y="6" width="8" height="14"/><path d="M8 20v6a4 4 0 0 0 8 0V10a4 4 0 0 1 8 0v20"/></svg><b>Cable Repair or Replacement:</b>Depending on the severity, we either re-pair the existing cables or replace them with new ones to restore full functional-ity.</div>
    <div class="step" style="top:194px"><svg viewBox="0 0 34 34" fill="none" stroke="#fff" stroke-width="1.8"><path d="M2 17L14 7l10 8"/><path d="M6 15v13h14V18"/><path d="M12 28v-7h4v7"/><circle cx="26" cy="16" r="6"/><path d="M23 16l2 2 4-4"/></svg><b>Sealing and Protection:</b>After repairing, we seal the affected areas to protect against moisture and future damage.</div>
    <div class="step" style="top:251px"><svg viewBox="0 0 34 34" fill="none" stroke="#fff" stroke-width="1.8"><circle cx="17" cy="14" r="10"/><path d="M17 9l1.6 3.4 3.6.4-2.7 2.4.8 3.6-3.3-1.9-3.3 1.9.8-3.6-2.7-2.4 3.6-.4z"/><path d="M11 22l-4 9 4-2 2 3 3-7M23 22l4 9-4-2-2 3-3-7"/></svg><b>Quality Assurance:</b>We perform rigorous quality checks to ensure the repairs meet industry standards and the structure is safe for use.</div>
  </section>

  <h2 class="abs section-head choose-head"><span class="g">WHY</span> <span class="s">CHOOSE US</span></h2>

  <ul class="abs points choose">
    <li><svg class="check" viewBox="0 0 12 12"><circle cx="6" cy="6" r="6" fill="#005c31"/><path d="M3.2 6.2l2 2 3.6-4" stroke="#fff" stroke-width="1.6" fill="none"/></svg><b>Expertise and Experience:</b>With years of experience in post-tension cable repair, our team is skilled in handling even the most complex repairs efficiently and effectively.</li>
    <li><svg class="check" viewBox="0 0 12 12"><circle cx="6" cy="6" r="6" fill="#005c31"/><path d="M3.2 6.2l2 2 3.6-4" stroke="#fff" stroke-width="1.6" fill="none"/></svg><b>Advanced Technology:</b>We use the latest technology and materials to ensure durable and long-lasting repairs.</li>
    <li><svg class="check" viewBox="0 0 12 12"><circle cx="6" cy="6" r="6" fill="#005c31"/><path d="M3.2 6.2l2 2 3.6-4" stroke="#fff" stroke-width="1.6" fill="none"/></svg><b>Customer Satisfaction:</b>Our commitment to quality and customer satisfaction sets us apart. We work closely with our clients to ensure their needs are met and expectations exceeded.</li>
  </ul>

  <p class="abs closing" style="top:1057px">If you suspect issues with your post-tension cables or need a routine inspection, don't hesitate to contact us. Our experts are ready to provide the best solutions to keep your structures safe and secure.</p>
  <p class="abs closing" style="top:1093px">Ensure the safety and longevity of your building with our professional post-tension cable repair services. Trust us to deliver quality and reliability every time.</p>

  <h2 class="abs contact-head"><span class="g">CONTACT</span><span class="s">US NOW</span></h2>
  <div class="abs contact-line" style="top:1130px"><svg viewBox="0 0 12 12"><rect width="12" height="12" rx="1.5" fill="#005c31"/><path d="M3.5 2.8l1.4 1.9-.8 1a5 5 0 0 0 2.2 2.2l1-.8 1.9 1.4-.8 1.2C5.7 9.6 2.4 6.3 2.3 3.6z" fill="#fff"/></svg>(555) 214-3870</div>
  <div class="abs contact-line" style="top:1154px"><svg viewBox="0 0 12 12"><rect width="12" height="12" rx="1.5" fill="#005c31"/><rect x="2.5" y="3.5" width="7" height="5" fill="none" stroke="#fff" stroke-width="1"/><path d="M2.5 3.5L6 6.3l3.5-2.8" fill="none" stroke="#fff" stroke-width="1"/></svg>info@ridgeviewcableworks.com</div>
  <div class="abs web">www.ridgeviewcableworks.com</div>
</main>
</body>
</html>
```